Plakate für TQ Car Wash
Zielgruppe
TQ Car Wash
SB Waschpark mit 4 Plätzen
Zielgruppe: Alle Autofahrer aus der Region
Marketing wg. Neueröffnung
Aufgabenstellung
Design ist für zwei Planen an einem Werbeanhänger
2200mm x 4750mm Fläche
Aussagen, Logo (kann ähnlich sein oder als eps bzw ai geliefert werden) als Ideenskizze in den Dateien mitgeliwfert. Open to new ideas.

```html
<!DOCTYPE html>
<html lang="de">
<head>
<meta charset="utf-8">
<title>Car Wash Neueröffnung – Plane</title>
<link rel="stylesheet" href="https://fonts.googleapis.com/css2?family=Archivo:wdth,wght@125,700;125,800;125,900&display=swap">
<style>
  :root {
    --navy: #003b6b;
    --sky: #1eaae2;
    --white: #ffffff;
    --bubble-light: #bfe6f7;
  }
  html, body {
    margin: 0;
    padding: 0;
    overflow: hidden;
    background: var(--white);
  }
  .banner {
    position: relative;
    width: 1200px;
    height: 555px;
    overflow: hidden;
    background: var(--white);
    box-sizing: border-box;
    border: 1px solid var(--navy);
  }
  .banner-art {
    position: absolute;
    inset: 0;
    width: 1200px;
    height: 555px;
    display: block;
  }
  .banner-art text {
    font-family: "Archivo", "Arial Black", sans-serif;
    font-stretch: 125%;
  }
  .headline { font-weight: 900; font-size: 160px; }
  .headline .word-car { fill: var(--navy); }
  .headline .word-wash { fill: var(--sky); }
  .opening { font-weight: 900; font-size: 48px; fill: var(--navy); }
  .pill-shape { fill: var(--sky); }
  .pill-label { font-weight: 800; font-size: 36px; fill: var(--white); }
  .footer-band { fill: var(--navy); }
  .footer-label { font-weight: 800; font-size: 40px; fill: var(--white); }
  .car-illustration { fill: url(#foamGradient); }
</style>
</head>
<body>
<main class="banner">
  <svg class="banner-art" viewBox="0 0 1200 555" xmlns="http://www.w3.org/2000/svg">
    <defs>
      <linearGradient id="foamGradient" x1="0" y1="0" x2="0" y2="1">
        <stop offset="0" stop-color="#1eaae2"/>
        <stop offset="0.55" stop-color="#bfe6f7"/>
        <stop offset="1" stop-color="#ffffff"/>
      </linearGradient>
    </defs>

    <text class="headline" x="31" y="143" textLength="1137" lengthAdjust="spacingAndGlyphs"><tspan class="word-car">CAR</tspan><tspan class="word-wash">WASH</tspan></text>

    <path class="car-illustration" role="img" aria-label="Illustration: weißes Auto im Profil vor hellblauem Seifenschaum mit Glitzersternen"
      d="M60,170 H590 Q612,170 612,192 V214 Q612,232 630,232 H738 Q762,232 762,256 V442 Q762,468 736,468 H57 Q31,468 31,442 V196 Q31,170 60,170 Z"/>

    <text class="opening" x="635" y="205" textLength="533" lengthAdjust="spacingAndGlyphs">NEUERÖFFNUNG</text>

    <g class="pill">
      <rect class="pill-shape" x="878" y="241" width="292" height="59" rx="29.5"/>
      <text class="pill-label" x="916" y="283" textLength="216" lengthAdjust="spacingAndGlyphs">EINFACH</text>
    </g>
    <g class="pill">
      <rect class="pill-shape" x="793" y="314" width="277" height="59" rx="29.5"/>
      <text class="pill-label" x="834" y="356" textLength="198" lengthAdjust="spacingAndGlyphs">BESSER</text>
    </g>
    <g class="pill">
      <rect class="pill-shape" x="850" y="387" width="284" height="59" rx="29.5"/>
      <text class="pill-label" x="889" y="428" textLength="206" lengthAdjust="spacingAndGlyphs">SAUBER</text>
    </g>

    <rect class="footer-band" x="0" y="488" width="1200" height="67"/>
    <text class="footer-label" x="29" y="533" textLength="1141" lengthAdjust="spacingAndGlyphs">BIRKENFEHN HINTER DER FEUERWEHR</text>
  </svg>
</main>
</body>
</html>
```